Flyer for Aluminium recycling business

We are a startup aluminium recycling business. We don’t have a logo yet. I’ve attached a flyer created by one of our sales people but it’s a bit average and we need something a bit more modern and slick. You have creative license to completely change everything - as long as the information being communicated is the same.

Target Market(s)

Hospitality, Hotels, Apartment blocks, malls etcs

Industry/Entity Type

Aluminium recycling

Requirements
Must have
• the wording
Nice to have
• you have free license on design aspect

```html
<!DOCTYPE html>
<html lang="en">
<head>
<meta charset="utf-8">
<title>Greenloop Metals – Aluminium Recycling Flyer</title>
<link href="https://fonts.googleapis.com/css2?family=Poppins:wght@300;400;500;700;800&display=swap" rel="stylesheet">
<style>
  :root {
    --paper: #e8e8e7;
    --ink: #1f1f1f;
    --forest: #3b6457;
    --brand-green: #3f9a3a;
    --card: #efefef;
    --blue: #3cb4ea;
    --red: #e7321f;
    --lime: #72e01b;
    --yellow: #eeea12;
    --slate: #6b7a7c;
    --badge-1: #f4b843;
    --badge-2: #d93a51;
    --badge-3: #3b9cb1;
    --badge-4: #2d5e97;
    --badge-5: #1f466b;
  }
  * { box-sizing: border-box; margin: 0; padding: 0; }
  html, body { width: 953px; height: 1200px; overflow: hidden; }
  body {
    background: var(--paper);
    font-family: "Poppins", sans-serif;
    color: var(--ink);
    position: relative;
  }
  .brand {
    position: absolute; top: 64px; left: 0; width: 100%;
    display: flex; align-items: center; justify-content: center; gap: 14px;
  }
  .brand-dot {
    width: 56px; height: 56px; border-radius: 50%;
    background: var(--brand-green);
  }
  .brand-name {
    font-family: "Poppins", sans-serif; font-weight: 500;
    font-size: 30px; line-height: 1; color: var(--forest);
  }
  .headline { position: absolute; top: 180px; left: 0; width: 100%; text-align: center; }
  .headline-lead { font-weight: 400; font-size: 52px; line-height: 1.2; }
  .headline-main {
    font-weight: 800; font-size: 60px; line-height: 0.92;
    color: var(--forest); letter-spacing: 0.5px; margin-top: 8px;
  }
  .tagline {
    position: absolute; top: 372px; left: 0; width: 100%;
    text-align: center; font-size: 23px; line-height: 1.3;
  }
  .step { position: absolute; width: 383px; height: 105px; }
  .step-panel {
    position: absolute; left: 40px; right: 0; top: 0; bottom: 0;
    background: var(--card);
    border-right: 8px solid var(--accent);
    border-radius: 0 22px 22px 0;
    box-shadow: 0 2px 4px rgba(0,0,0,0.06);
  }
  .step-icon {
    position: absolute; left: 0; top: -4px;
    width: 113px; height: 113px; border-radius: 50%;
    background: #fff;
    box-shadow: 0 2px 5px rgba(0,0,0,0.15);
    display: flex; align-items: center; justify-content: center;
  }
  .step-icon .ring {
    width: 103px; height: 103px; border-radius: 50%;
    background: var(--tone);
    display: flex; align-items: center; justify-content: center;
  }
  .step-icon .core {
    width: 74px; height: 74px; border-radius: 50%;
    border: 2px solid #fff;
    display: flex; align-items: center; justify-content: center;
  }
  .step-text {
    position: absolute; left: 131px; width: 180px; top: 0; bottom: 0;
    display: flex; align-items: center;
    font-size: 10.5px; line-height: 1.42; color: #2a2a2a;
  }
  .step-num {
    position: absolute; right: 8px; top: 37px;
    width: 60px; height: 32px; border-radius: 16px 0 0 16px;
    background: var(--accent); color: #fff;
    font-weight: 700; font-size: 20px; line-height: 32px; padding-left: 12px;
  }
  .step-1 { left: 69px; top: 483px; --tone: var(--blue); --accent: var(--badge-1); }
  .step-2 { left: 69px; top: 626px; --tone: var(--red); --accent: var(--badge-2); }
  .step-3 { left: 69px; top: 753px; --tone: var(--lime); --accent: var(--badge-3); }
  .step-4 { left: 484px; top: 483px; --tone: var(--yellow); --accent: var(--badge-4); }
  .step-5 { left: 484px; top: 626px; --tone: var(--slate); --accent: var(--badge-5); }
  .accepted { position: absolute; left: 73px; top: 913px; }
  .accepted h2 { font-weight: 700; font-size: 25px; color: var(--forest); margin-bottom: 8px; }
  .accepted ul { list-style: none; }
  .accepted li {
    font-size: 12.8px; line-height: 21.6px; display: flex; align-items: center; gap: 6px;
  }
  .accepted svg { flex: none; }
  .bin-photo {
    position: absolute; left: 492px; top: 770px; width: 374px; height: 430px;
    background: linear-gradient(180deg, #c9ccd0 0%, #2aa33a 14%, #0d8a22 80%, #d8d6cc 100%);
    border-radius: 8px 8px 0 0;
  }
</style>
</head>
<body>
  <header class="brand">
    <span class="brand-dot"></span>
    <span class="brand-name">Greenloop Metals</span>
  </header>

  <section class="headline">
    <p class="headline-lead">Playing the fair</p>
    <h1 class="headline-main">ALUMINIUM RECYCLING<br>GAME FOR GOOD</h1>
  </section>

  <p class="tagline">Our partnership with you is based on common sense,<br>mutual gain and a better tomorrow</p>

  <div class="step step-1">
    <div class="step-panel"></div>
    <div class="step-icon"><div class="ring"><div class="core">
      <svg width="34" height="38" viewBox="0 0 34 38" fill="none" stroke="#fff" stroke-width="3"><path d="M4 9h26M12 9V4h10v5M7 9l2 26h16l2-26M14 15v14M20 15v14"/></svg>
    </div></div></div>
    <p class="step-text">We bring you a free bin</p>
    <span class="step-num">01</span>
  </div>

  <div class="step step-2">
    <div class="step-panel"></div>
    <div class="step-icon"><div class="ring"><div class="core">
      <svg width="40" height="36" viewBox="0 0 40 36" fill="#fff"><rect x="3" y="8" width="14" height="24" rx="2"/><rect x="22" y="4" width="15" height="28" rx="2"/></svg>
    </div></div></div>
    <p class="step-text">You throw all and any aluminium waste into the bin - no need to super-clean it. Try to compact / squash the aluminium as much as possible</p>
    <span class="step-num">02</span>
  </div>

  <div class="step step-3">
    <div class="step-panel"></div>
    <div class="step-icon"><div class="ring"><div class="core">
      <svg width="40" height="40" viewBox="0 0 40 40" fill="none" stroke="#fff" stroke-width="3"><circle cx="20" cy="14" r="9"/><path d="M4 30h10l6 4 14-6"/></svg>
    </div></div></div>
    <p class="step-text">We collect the bin at no charge</p>
    <span class="step-num">03</span>
  </div>

  <div class="step step-4">
    <div class="step-panel"></div>
    <div class="step-icon"><div class="ring"><div class="core">
      <svg width="40" height="40" viewBox="0 0 40 40" fill="none" stroke="#fff" stroke-width="3"><circle cx="20" cy="20" r="13"/><circle cx="20" cy="20" r="4" fill="#fff"/></svg>
    </div></div></div>
    <p class="step-text">We turn the aluminium waste into a desirable resource</p>
    <span class="step-num">04</span>
  </div>

  <div class="step step-5">
    <div class="step-panel"></div>
    <div class="step-icon"><div class="ring"><div class="core">
      <svg width="40" height="40" viewBox="0 0 40 40" fill="none" stroke="#fff" stroke-width="3"><rect x="8" y="8" width="24" height="14" rx="2"/><path d="M8 30h24l-5-4"/></svg>
    </div></div></div>
    <p class="step-text">We pay you for however much of that resource your waste has generated - and give you a report on that, so you can see how good you are</p>
    <span class="step-num">05</span>
  </div>

  <section class="accepted">
    <h2>Examples of what we can take</h2>
    <ul>
      <li><svg width="12" height="12" viewBox="0 0 12 12"><path d="M1 6l3 4 7-9" fill="none" stroke="#3b6457" stroke-width="2"/></svg>Used beverage cans - any</li>
      <li><svg width="12" height="12" viewBox="0 0 12 12"><path d="M1 6l3 4 7-9" fill="none" stroke="#3b6457" stroke-width="2"/></svg>Tinfoil - scrunched, crusty, burned or dirty</li>
      <li><svg width="12" height="12" viewBox="0 0 12 12"><path d="M1 6l3 4 7-9" fill="none" stroke="#3b6457" stroke-width="2"/></svg>Disposable BBQ roasting trays</li>
      <li><svg width="12" height="12" viewBox="0 0 12 12"><path d="M1 6l3 4 7-9" fill="none" stroke="#3b6457" stroke-width="2"/></svg>Aluminium takeaway containers</li>
      <li><svg width="12" height="12" viewBox="0 0 12 12"><path d="M1 6l3 4 7-9" fill="none" stroke="#3b6457" stroke-width="2"/></svg>Wine bottle screw tops (and collars - if you can get them off)</li>
      <li><svg width="12" height="12" viewBox="0 0 12 12"><path d="M1 6l3 4 7-9" fill="none" stroke="#3b6457" stroke-width="2"/></svg>Podvella (or any other aluminium) coffee pods</li>
      <li><svg width="12" height="12" viewBox="0 0 12 12"><path d="M1 6l3 4 7-9" fill="none" stroke="#3b6457" stroke-width="2"/></svg>Tear-off can lids</li>
      <li><svg width="12" height="12" viewBox="0 0 12 12"><path d="M1 6l3 4 7-9" fill="none" stroke="#3b6457" stroke-width="2"/></svg>Old / broken Lumo-Pads, tablets, laptops or cell phones</li>
    </ul>
  </section>

  <div class="bin-photo" role="img" aria-label="Photo of a green recycling bin filled with crushed aluminium cans, with a stack of banknotes beside it"></div>
</body>
</html>
```